Company or website name
- marissatelkovitz.com
- Links to the website
- marissatelkovitz.com
- Describe your company and organization and target audience
- Hi, my name is Marissa. I do comedy jokes. Sometimes I do them on a stage. Sometimes I am paid to write them down on paper. And sometimes I stand somewhere offstage and direct. I am wanting to have a cool website that highlights my different skill sets, holds video content, photos, contact info, resume stuff, and other things that I'm forgetting right now. I want it to be friendly, smart, dare I say, FUNNY? But not corny. My target audience would be comedy bookers, event planners, agents, managers, and anyone stopping by to judge me. Ha.
- The design should have the following
- I think there might be 3 or four different pages.. 1. main page with contact info, bio 2. stand-up comedy page with upcoming shows and demo reel 3. acting page with photos/resume/demo reel 3. Directing/writing/teaching page with photos and client satisfaction blurbs. I'm open though to your expertise and creativity. Thanks for giving it a go!!

```html
<!DOCTYPE html>
<html lang="en">
<head>
<meta charset="utf-8">
<title>Marissa Telkovitz</title>
<link rel="stylesheet" href="https://fonts.googleapis.com/css2?family=Raleway:wght@400;500;600&display=swap">
<style>
  :root {
    --hero-top: #b4bdc4;
    --hero-bottom: #7e8c98;
    --tab-idle: #55616a;
    --tab-active: #8c3b88;
    --bio-light: #e6e1f0;
    --bio-mid: #8358c8;
    --bio-deep: #5a2d8c;
    --footer: #4e5a62;
    --footer-text: #b9c1c7;
    --white: #ffffff;
    --photo-skin: #d2a48c;
    --photo-hair: #5a3a2a;
    --photo-sweater: #8fb0d8;
    --photo-bio-a: #a494bf;
    --photo-bio-b: #6b5a86;
  }
  * { box-sizing: border-box; margin: 0; padding: 0; }
  html, body { width: 1200px; height: 752px; overflow: hidden; }
  body { font-family: "Raleway", sans-serif; color: var(--white); background: var(--white); }
  .page { position: relative; width: 1200px; height: 752px; }

  .hero {
    position: absolute; left: 0; top: 0; width: 1200px; height: 448px;
    background: linear-gradient(180deg, var(--hero-top) 0%, var(--hero-bottom) 100%);
    overflow: hidden;
  }
  .hero-social { position: absolute; left: 50px; top: 36px; }
  .hero-portrait {
    position: absolute; right: 0; top: 0; width: 500px; height: 448px;
    background:
      radial-gradient(ellipse 95px 120px at 62% 30%, var(--photo-skin) 0%, rgba(210,164,140,.85) 55%, rgba(210,164,140,0) 100%),
      radial-gradient(ellipse 150px 150px at 60% 22%, rgba(90,58,42,.9) 0%, rgba(90,58,42,.5) 60%, rgba(90,58,42,0) 100%),
      radial-gradient(ellipse 260px 150px at 65% 105%, var(--photo-sweater) 0%, rgba(143,176,216,.8) 60%, rgba(143,176,216,0) 100%);
    -webkit-mask-image: linear-gradient(90deg, transparent 0%, #000 30%);
    mask-image: linear-gradient(90deg, transparent 0%, #000 30%);
  }
  .wordmark {
    position: absolute; left: 190px; top: 186px; width: 540px;
    font-weight: 400; font-size: 58px; letter-spacing: 3px; text-align: center;
    color: var(--white);
  }

  .main-nav { position: absolute; left: 91px; top: 426px; display: flex; gap: 11px; }
  .main-nav a {
    display: block; width: 131px; height: 22px; line-height: 22px;
    background: var(--tab-idle); color: var(--white); text-decoration: none;
    text-align: center; font-size: 12px; font-weight: 600; letter-spacing: .6px;
  }
  .main-nav a.is-active { background: var(--tab-active); }

  .bio {
    position: absolute; left: 0; top: 448px; width: 1200px; height: 280px;
    background: linear-gradient(90deg, var(--bio-light) 0%, #b9a5de 25%, var(--bio-mid) 60%, var(--bio-deep) 100%);
  }
  .bio-portrait {
    position: absolute; left: 140px; top: 0; width: 270px; height: 280px;
    background:
      radial-gradient(ellipse 80px 100px at 50% 48%, #b6a8cc 0%, rgba(182,168,204,0) 100%),
      radial-gradient(ellipse 130px 150px at 50% 40%, var(--photo-bio-b) 0%, rgba(107,90,134,.6) 70%, rgba(107,90,134,0) 100%);
  }
  .bio-text {
    position: absolute; left: 524px; top: 27px; width: 456px;
    font-size: 15.5px; line-height: 18.6px;
  }
  .bio-text p + p { margin-top: 18.6px; }

  .site-footer {
    position: absolute; left: 0; top: 728px; width: 1200px; height: 24px;
    background: var(--footer);
  }
  .copyright {
    position: absolute; left: 58px; top: 0; line-height: 24px;
    font-size: 8px; color: var(--footer-text);
  }
  .footer-social { position: absolute; left: 1044px; top: 3px; }
</style>
</head>
<body>
<div class="page">
  <header class="hero">
    <div class="hero-portrait" role="img" aria-label="Photo of Marissa making a comically disgusted face"></div>
    <svg class="hero-social" width="184" height="28" viewBox="0 0 184 28" aria-label="Contact links">
      <g fill="none" stroke="#ffffff" stroke-width="1.5" stroke-linecap="round" stroke-linejoin="round">
        <circle cx="14" cy="14" r="12"/>
        <rect x="8.5" y="10" width="11" height="8" rx="1"/><path d="M8.5 10.5 14 15l5.5-4.5"/>
        <circle cx="52" cy="14" r="12"/>
        <path d="M48 9.5c0 5 3.5 9 8.5 9l1-2.5-2.5-1.5-1.5 1.5c-1.5-.7-2.8-2-3.5-3.5l1.5-1.5-1.5-2.5z"/>
        <circle cx="90" cy="14" r="12"/>
        <path d="M90 20s-4.5-4.5-4.5-8a4.5 4.5 0 0 1 9 0c0 3.5-4.5 8-4.5 8z"/><circle cx="90" cy="12" r="1.5"/>
        <circle cx="128" cy="14" r="12"/>
        <rect x="121.5" y="11.5" width="7" height="5" rx="2.5"/><rect x="127.5" y="11.5" width="7" height="5" rx="2.5"/>
        <circle cx="166" cy="14" r="12"/>
        <path d="M160.5 14h11M167.5 10l4 4-4 4"/>
      </g>
    </svg>
    <div class="wordmark">Marissa Telkovitz</div>
  </header>

  <nav class="main-nav">
    <a href="#" class="is-active">BIO</a>
    <a href="#">UPCOMING SHOWS</a>
    <a href="#">GALLERY</a>
    <a href="#">SPECIAL</a>
    <a href="#">CONTACT</a>
  </nav>

  <section class="bio">
    <div class="bio-portrait" role="img" aria-label="Smiling headshot of Marissa, tinted purple"></div>
    <div class="bio-text">
      <p>Marissa Telkovitz is an advocate of fun, living in and around Los Angeles, California. In recent years, she has been spotted writing at her computer in food-stained sweatpants, being pulled around the neighborhood by her skittish dog, directing odd events at Wonderfair Park, buying lesser known cheeses at Grocer Pete's, portraying quirky characters in fringe theater spaces, teaching 'the basics of not looking like an asshole onstage' to hormonal teenagers, and perusing the self-help aisle at Page &amp; Quill.</p>
      <p>When Marissa grows up, she wants to be able to contain her laughter in serious situations.</p>
    </div>
  </section>

  <footer class="site-footer">
    <div class="copyright">Copyright © 2015. Marissa Telkovitz, Inc. All Rights Reserved. | Terms and Conditions</div>
    <svg class="footer-social" width="100" height="18" viewBox="0 0 100 18" aria-label="Contact links">
      <g fill="none" stroke="#ffffff" stroke-width="1.1" stroke-linecap="round" stroke-linejoin="round">
        <circle cx="9" cy="9" r="7"/><rect x="5.8" y="6.8" width="6.4" height="4.6" rx=".6"/><path d="M5.8 7.2 9 9.7l3.2-2.5"/>
        <circle cx="29" cy="9" r="7"/><path d="M26.8 6.3c0 3 2 5.3 4.9 5.3l.5-1.4-1.4-.9-.9.9c-.9-.4-1.6-1.1-2-2l.9-.9-.9-1.4z"/>
        <circle cx="50" cy="9" r="7"/><path d="M50 12.6s-2.6-2.6-2.6-4.6a2.6 2.6 0 0 1 5.2 0c0 2-2.6 4.6-2.6 4.6z"/>
        <circle cx="70" cy="9" r="7"/><rect x="66.2" y="7.5" width="4.2" height="3" rx="1.5"/><rect x="69.6" y="7.5" width="4.2" height="3" rx="1.5"/>
        <circle cx="91" cy="9" r="7"/><path d="M87.8 9h6.4M91.8 6.6 94.2 9l-2.4 2.4"/>
      </g>
    </svg>
  </footer>
</div>
</body>
</html>
```